Torvane PT Business Card

I need the card to be bright/bold colours to stand out amongst others.
It needs to have my company logo.
I was not interested in pictures etc just a layout that attracts attention.

I have attached my old design which is very plain. I also needed change the contact details. And my description changed to Personal Trainer
Phone 0427391058
Facebook Torvane PT
No email address please, no street address.
And only Torvane PT (Please remove anything to do with Torvane Supplements)

```html
<!DOCTYPE html>
<html lang="en">
<head>
<meta charset="utf-8">
<title>Torvane PT Business Card</title>
<link rel="stylesheet" href="https://fonts.googleapis.com/css2?family=Source+Sans+3:wght@400;600;700;800&display=swap">
<style>
  :root {
    --backdrop-top: #b3b3b3;
    --backdrop-bottom: #a2a2a2;
    --brand-blue: #0a87ca;
    --brand-yellow: #ffe11a;
    --paper: #ffffff;
    --ink-dark: #3a3a3a;
    --ink-light: #ffffff;
  }
  * { box-sizing: border-box; margin: 0; padding: 0; }
  html, body { width: 1200px; height: 900px; overflow: hidden; }
  body {
    background: linear-gradient(180deg, var(--backdrop-top), var(--backdrop-bottom));
    font-family: "Source Sans 3", sans-serif;
    position: relative;
  }
  .card {
    position: absolute;
    top: 306px;
    width: 439px;
    height: 271px;
    border-radius: 10px;
    overflow: hidden;
    box-shadow: 0 1px 3px rgba(0,0,0,0.18);
  }
  .card--front { left: 149px; background: var(--paper); }
  .card--back { left: 609px; background: var(--brand-blue); }

  /* Front */
  .front-header { position: absolute; left: 0; top: 0; width: 100%; height: 126px; background: var(--paper); }
  .front-stripe { position: absolute; left: 0; top: 126px; width: 100%; height: 6px; background: var(--brand-yellow); }
  .front-body { position: absolute; left: 0; top: 132px; width: 100%; bottom: 0; background: var(--brand-blue); }

  .brand-name {
    font-weight: 800;
    letter-spacing: 0.5px;
    line-height: 1;
    white-space: nowrap;
  }
  .card--front .brand-name {
    position: absolute; left: 23px; top: 40px;
    font-size: 38px; color: var(--brand-blue);
  }
  .owner { position: absolute; right: 22px; top: 49px; text-align: right; }
  .owner-name { font-size: 16px; font-weight: 600; line-height: 1; letter-spacing: 0.2px; }
  .owner-first { color: var(--brand-yellow); }
  .owner-last { color: var(--brand-blue); }
  .owner-role { font-size: 12.5px; color: var(--ink-dark); margin-top: 3px; }

  .contact-list { position: absolute; left: 21px; top: 36px; list-style: none; color: var(--ink-light); font-size: 12.5px; }
  .contact-item { display: flex; align-items: center; height: 16px; }
  .contact-item--social { font-size: 13px; margin-bottom: 16px; }
  .contact-icon { width: 14px; height: 14px; margin-right: 6px; flex: none; }
  .contact-item--social .social-square { width: 14px; height: 14px; background: var(--ink-light); border-radius: 2px; margin-right: 6px; flex: none; }

  /* Back */
  .card--back .brand-name {
    position: absolute; left: 0; right: 0; top: 100px;
    text-align: center; font-size: 52px; color: var(--ink-light);
  }
</style>
</head>
<body>
  <section class="card card--front" aria-label="Business card front">
    <div class="front-header"></div>
    <div class="front-stripe"></div>
    <div class="front-body">
      <ul class="contact-list">
        <li class="contact-item contact-item--social"><span class="social-square"></span>Torvane PT</li>
        <li class="contact-item">
          <svg class="contact-icon" viewBox="0 0 14 14" aria-hidden="true"><path fill="#fff" d="M3.2 2.2l1.7-.4 1 2.4-1.1.9a7 7 0 0 0 3.1 3.1l.9-1.1 2.4 1-.4 1.7c-.2.5-.7.8-1.2.7A8.6 8.6 0 0 1 2.5 3.4c-.1-.5.2-1 .7-1.2z"/></svg>
          0427391058
        </li>
      </ul>
    </div>
    <div class="brand-name">TORVANE PT</div>
    <div class="owner">
      <p class="owner-name"><span class="owner-first">DEAN</span> <span class="owner-last">HARLOW</span></p>
      <p class="owner-role">Personal Trainer</p>
    </div>
  </section>

  <section class="card card--back" aria-label="Business card back">
    <div class="brand-name">TORVANE PT</div>
  </section>
</body>
</html>
```